Cobalt Ridge Energy

Design a 330ml Energy drink pack. Brand Name is 6/40 (meaning Energy lasting 24hrs a day and 7 days a week). The background colour should be silver and a touch of red, very similar but premium to to Tarvo Falcon attached. The logo should be a red or black elephant (see samples attached)
The pay-off should be "Feel Good" and "Long Lasting Energy",
at the bottom of the can like teal moth, written in red. Let the font be Cambria or a better option. Can should have complete ingredient listing, space for bar code, manufacturer and brand owners

Target Market(s)

Mainstream Market

Industry/Entity Type

Manufacturer

Requirements
Must have
• Must have strong presence on the shelve

```html
<!DOCTYPE html>
<html lang="en">
<head>
<meta charset="utf-8">
<title>6/40 Energy Drink – Can Wrap</title>
<link rel="stylesheet" href="https://fonts.googleapis.com/css2?family=Caladea:wght@400;700&display=swap">
<style>
  :root {
    --can-red: #e62128;
    --can-gold: #ebb748;
    --can-silver: #a7afba;
    --brand-navy: #0f416b;
    --label-white: #ffffff;
    --serif: "Caladea", Cambria, Georgia, serif;
  }
  html, body {
    margin: 0;
    padding: 0;
    overflow: hidden;
    background: var(--can-silver);
  }
  .can-wrap {
    position: relative;
    width: 1200px;
    height: 2226px;
    overflow: hidden;
    background: var(--can-silver);
    font-family: var(--serif);
  }
  .band-red {
    position: absolute; left: 0; top: 0;
    width: 1200px; height: 557px;
    background: var(--can-red);
  }
  .band-gold {
    position: absolute; left: 0; top: 557px;
    width: 1200px; height: 259px;
    background: var(--can-gold);
  }
  .graphics {
    position: absolute; inset: 0;
  }
  .product-type {
    position: absolute; left: 0; top: 178px;
    width: 1200px;
    margin: 0;
    text-align: center;
    color: var(--can-gold);
    font-size: 116px;
    font-weight: 700;
    letter-spacing: 7px;
    line-height: 1;
  }
  .owner-badge {
    position: absolute; left: 59px; top: 469px;
    width: 457px; height: 459px;
    background: var(--brand-navy);
    display: flex;
    align-items: center;
    justify-content: center;
  }
  .owner-name {
    color: var(--label-white);
    font-size: 62px;
    font-weight: 700;
    text-align: center;
    line-height: 1.1;
  }
  .brand-name {
    position: absolute; left: 612px; top: 470px;
    width: 540px;
    margin: 0;
    text-align: center;
    color: var(--brand-navy);
    font-size: 206px;
    font-weight: 400;
    letter-spacing: 22px;
    line-height: 1;
  }
  .payoff-feel-good {
    position: absolute;
    left: 788px; top: 965px;
    transform: translate(-50%, -50%) rotate(-43deg);
    white-space: nowrap;
    color: var(--can-red);
    font-size: 98px;
    letter-spacing: 4px;
    line-height: 1;
  }
  .payoff-long-lasting {
    position: absolute;
    left: 600px; top: 1560px;
    transform: translate(-50%, -50%) rotate(46deg);
    white-space: nowrap;
    color: var(--can-gold);
    -webkit-text-stroke: 3px var(--brand-navy);
    paint-order: stroke fill;
    font-size: 112px;
    font-weight: 700;
    letter-spacing: 5px;
    line-height: 1;
  }
</style>
</head>
<body>
<main class="can-wrap">
  <div class="band-red"></div>
  <div class="band-gold"></div>

  <svg class="graphics" width="1200" height="2226" viewBox="0 0 1200 2226">
    <g class="mascot-area" role="img" aria-label="Red and white illustrated elephant mascot walking to the left">
      <ellipse cx="640" cy="1560" rx="470" ry="330" fill="var(--can-red)"/>
      <rect x="170" y="1620" width="830" height="560" rx="90" fill="var(--can-red)"/>
    </g>
    <line class="accent-line-red" x1="779" y1="1261" x2="1200" y2="909" stroke="var(--can-red)" stroke-width="5"/>
    <line class="accent-line-gold" x1="0" y1="1261" x2="872" y2="2226" stroke="var(--brand-navy)" stroke-width="10"/>
    <line class="accent-line-gold-core" x1="0" y1="1261" x2="872" y2="2226" stroke="var(--can-gold)" stroke-width="5"/>
  </svg>

  <h2 class="product-type">Energy Drink</h2>

  <div class="owner-badge">
    <span class="owner-name">Meridian Vault</span>
  </div>

  <h1 class="brand-name">6/40</h1>

  <p class="payoff-feel-good">Feel Good</p>
  <p class="payoff-long-lasting">Long Lasting Energy</p>
</main>
</body>
</html>
```